I work in creative/artistic projects across different mediums.
It needs to communicate creativity, style, sexy, uniqueness, individuality and sophistication.
It should not look corporate.
Colours I like are black silver gold deep purple, chocolate, orchid.
It doesn't have to make use of all these colours.
I do not like bright primary colors.
Updates

Project Deadline Extended
Reason: Still in the communication process and to allow the person enough time to finish the design. Though i should know in the next day or two. Thank you.

Target Market(s)

creatives and companies wanting to inject creativity into thier business.

Industry/Entity Type

Work

Contact Information for Business Card

Lionel Crowthwick
0418359026
lionel@lionelcrowthwick.com

quietsilverhour.com.au

Requirements
Should not have
• Anything corporate OR OLD FASHIONED

```html
<!DOCTYPE html>
<html lang="en">
<head>
<meta charset="utf-8">
<title>Lionel Crowthwick — Business Card</title>
<link rel="stylesheet" href="https://fonts.googleapis.com/css2?family=Questrial&family=Arimo&display=swap">
<style>
  :root {
    --backdrop: #4b4746;
    --card-black: #0b0b0b;
    --card-edge: #0f0f0f;
    --inner-band: #201a18;
    --gold: #c8a564;
    --gold-light: #e2c98e;
    --ring-tone: #5b1d12;
    --ring-tone-dark: #3a100a;
  }
  html, body {
    margin: 0;
    padding: 0;
    width: 1200px;
    height: 1000px;
    overflow: hidden;
    background: var(--backdrop);
  }
  .canvas {
    position: relative;
    width: 1200px;
    height: 1000px;
  }
  .card {
    position: absolute;
    left: 44px;
    top: 155px;
    width: 1110px;
    height: 683px;
    background: var(--card-edge);
  }
  .card-band {
    position: absolute;
    left: 24px;
    top: 23px;
    width: 1062px;
    height: 637px;
    background: var(--inner-band);
  }
  .card-face {
    position: absolute;
    left: 36px;
    top: 35px;
    width: 1022px;
    height: 597px;
    border: 8px solid var(--gold);
    box-sizing: content-box;
    background:
      radial-gradient(ellipse 900px 260px at 820px 60px, rgba(255,255,255,0.06), rgba(255,255,255,0) 70%),
      var(--card-black);
    overflow: hidden;
  }
  .emblem {
    position: absolute;
    left: 140px;
    top: 255px;
    width: 440px;
    height: 440px;
  }
  .emblem-name {
    position: absolute;
    left: 140px;
    top: 255px;
    width: 440px;
    height: 440px;
    display: flex;
    flex-direction: column;
    align-items: center;
    justify-content: center;
    font-family: "Questrial", sans-serif;
    color: var(--gold);
    font-size: 58px;
    line-height: 1.2;
    text-align: center;
  }
  .contact {
    position: absolute;
    font-family: "Arimo", sans-serif;
    color: var(--gold);
    white-space: nowrap;
    line-height: 1;
  }
  .contact-phone { left: 734px; top: 646px; font-size: 33px; }
  .contact-email { left: 597px; top: 729px; font-size: 32px; }
  .contact-web   { left: 108px; top: 734px; font-size: 30px; }
</style>
</head>
<body>
<div class="canvas">
  <div class="card">
    <div class="card-band"></div>
    <div class="card-face"></div>
  </div>

  <svg class="emblem" viewBox="0 0 440 440" aria-hidden="false">
    <defs>
      <radialGradient id="ring-fill" cx="50%" cy="50%" r="50%">
        <stop offset="78%" stop-color="var(--ring-tone-dark)"/>
        <stop offset="90%" stop-color="var(--ring-tone)"/>
        <stop offset="100%" stop-color="var(--ring-tone-dark)"/>
      </radialGradient>
    </defs>
    <circle cx="220" cy="220" r="212" fill="none" stroke="var(--gold)" stroke-width="8"/>
    <path role="img" aria-label="Ornamental band of gold floral scrolls on deep red-brown"
          d="M220 12 A208 208 0 1 1 219.9 12 Z M220 52 A168 168 0 1 0 220.1 52 Z"
          fill="url(#ring-fill)" fill-rule="evenodd"/>
    <circle cx="220" cy="220" r="166" fill="var(--card-black)" stroke="var(--gold)" stroke-width="8"/>
    <path d="M40 150 A200 200 0 0 1 330 45" fill="none" stroke="var(--gold-light)" stroke-opacity="0.35" stroke-width="6"/>
  </svg>

  <div class="emblem-name">
    <span>Lionel</span>
    <span>Crowthwick</span>
  </div>

  <div class="contact contact-phone">0418359026</div>
  <div class="contact contact-email">lionel@lionelcrowthwick.com</div>
  <div class="contact contact-web">quietsilverhour.com.au</div>
</div>
</body>
</html>
```